Market place for used airplanes/helicopters/parts

http://www.vingtorget.se needs a facelift.

# What is it
Classifieds for used airplanes/helicopters/parts/spare parts/aviation literature, for people in Scandinavia. The number of classifieds is ~120-200. They are mainly in Swedish, English, Norwegian.

It's not a glamorous or luxurious business, but more for people with a genuine interest in flying, technical things.

Similar to sites like this, but they have much more classifieds than my site
http://www.skyquarry.com/list/list.aspx?ETID=1&setype=1&catid=6
http://www.lindqvistflyg.com/planes.asp?meny=1&typ=single
https://www.propwashdeals.com/cat.php?mode=listing&main=

# What I want
Design only - no code. I want a modern, maybe a bit bootstrap like, clean, simple, not flashy, web design. I want the design to be in English.

# Audience of the website
Aviation interested men, 45-65 years old, in the nordic countries (around Sweden).

# Logotype that could be used (but not necessarily)
http://www.vingtorget.se/flygplan_till_salu_large.jpg
http://www.vingtorget.se/flygplan_till_salu.eps

Reason: I decided to extend the deadline with 1 day. The reason is that I (unfortunately) managed to put the contest in the wrong category for 1 day + I want to give you all feedback (been too busy the whole day, sorry).

Hi all! 

Thanks everyone for the contributions you made. 

I will setup a poll for the designs that I like most. Will get back when I have more information. 

Thanks and have a nice weekend!
Kjell

Target Market(s)

45-65 old Scandinavian men

Industry/Entity Type

Business

Requirements
Must have
• - A list with classifieds on the first page, so the visitor easily can see new classifieds.
- A classifieds should be able to have more than one photo
- A simple navigation for showing classifieds from categories like airplanes, helicopters/gyrocopters, parts, literature, misc (maybe other categories) .... but still, it's just 100-200 ads so it's not needed that much filtration.

- A placeholder/way of showing aviation news/clips. In the old design I had, it was a column to the right. It's enough to show maybe 2-5 placeholders.
- A placeholder for PlaceAds ads somewhere on the site.
Should not have
• - Carousels
- Too much clutter

```html
<!DOCTYPE html>
<html lang="en">
<head>
<meta charset="utf-8">
<title>Vingtorget – Aircraft for Sale</title>
<link rel="stylesheet" href="https://fonts.googleapis.com/css2?family=Source+Sans+3:wght@300;400;600&family=Cousine&display=swap">
<style>
:root{
  --blue:#1a5ea8;
  --nav:#12a0e3;
  --nav-active:#0b4f9a;
  --text:#555;
  --muted:#777;
  --line:#ddd;
  --ink:#333;
  --footer:#111;
  --ad-link:#1a1aa6;
  --ad-url:#118a11;
}
*{box-sizing:border-box;margin:0;padding:0}
html,body{width:1200px;height:2429px;overflow:hidden;background:#fff}
body{font-family:"Source Sans 3",Arial,sans-serif;color:var(--text);position:relative}
.wrap{position:absolute;left:86px;width:1027px}

.site-header{top:0;height:150px}
.brand{position:absolute;left:0;top:58px;display:flex;align-items:center;gap:14px}
.brand-mark{width:30px;height:30px;background:var(--nav)}
.brand-name{font-size:44px;font-weight:600;color:var(--blue);letter-spacing:1px}
.account-links{position:absolute;right:0;top:78px;display:flex;font-size:18px;color:var(--ink)}
.account-links span{padding:0 12px;border-left:1px solid #999;line-height:18px}
.account-links span:first-child{border-left:0}
.account-links span:last-child{padding-right:0}

.main-nav{top:151px;height:53px;background:var(--nav);display:flex;align-items:center}
.main-nav .item{position:absolute;top:0;height:53px;line-height:53px;color:#fff;font-size:18px}
.main-nav .active{left:0;width:149px;background:var(--nav-active);text-align:center}
.search{position:absolute;left:792px;top:9px;width:224px;height:36px;background:#fff;display:flex;align-items:center;padding:0 12px;font-size:13px;color:#aaa;font-style:italic}
.search svg{margin-left:auto}

.intro{top:240px;text-align:center}
.intro h1{font-weight:400;font-size:26px;color:var(--blue);margin-bottom:14px}
.intro p{font-size:14.5px;line-height:25px;font-weight:300;color:#444;padding:0 4px}

.listing{position:absolute;width:301px;height:431px}
.listing .photo{height:202px}
.listing .head{display:flex;justify-content:space-between;margin-top:28px;font-size:16px}
.listing .title{color:var(--blue)}
.listing .date{color:var(--muted);font-size:14px;font-weight:300}
.listing .desc{margin-top:12px;font-size:14px;line-height:25px;font-weight:300;color:#444}
.listing hr{border:0;border-top:1px solid var(--line);margin:14px 0 16px}
.seller{display:flex;gap:28px}
.seller .avatar{width:74px;height:60px}
.seller .name{font-size:17px;color:var(--blue);line-height:20px}
.seller dl{font-size:13px;color:var(--muted);font-weight:300;line-height:23px;display:grid;grid-template-columns:68px auto}

.pager{top:1890px;display:flex;justify-content:flex-end;gap:8px}
.pager span{height:26px;min-width:26px;padding:0 7px;border:1px solid #ccc;background:#f3f3f3;font-size:12px;line-height:24px;color:#444;text-align:center}

.news{top:1945px;width:580px}
.news h2{font-weight:400;font-size:27px;color:var(--blue);margin-bottom:20px}
.news-item{display:flex;gap:24px;margin-bottom:24px}
.news-item .thumb{width:132px;height:124px;border:1px solid #ccc;padding:4px;flex:none}
.news-item .thumb div{width:100%;height:100%}
.news-item h3{font-size:17px;font-weight:600;color:var(--blue);margin:-2px 0 4px}
.news-item p{font-size:13px;line-height:20px;color:#333}
.news-item small{display:block;margin-top:10px;font-size:11px;font-style:italic;color:#444}

.ad-box{position:absolute;left:693px;top:1993px;width:334px;height:270px;background:#f0f0f0;padding:14px 16px;font-family:Cousine,monospace}
.ad-box .tag{position:absolute;right:10px;top:10px;font-size:12px;font-family:Arial,sans-serif;color:#555}
.ad-box .ad{margin-top:22px}
.ad-box .ad h4{font-weight:400;font-family:Arial,sans-serif;font-size:19px;color:var(--ad-link)}
.ad-box .ad p{font-size:14px;line-height:19px;color:#333}
.ad-box .ad b{font-size:14px;color:var(--ad-url)}
.ad-box .provider{position:absolute;right:16px;bottom:14px;font-family:"Source Sans 3",sans-serif;font-size:20px;color:#555}

.site-footer{position:absolute;left:0;top:2312px;width:1200px;height:117px;background:var(--footer);color:#ddd;font-size:13px}
.site-footer .links{position:absolute;left:88px;top:30px}
.site-footer .copy{position:absolute;left:88px;top:63px}
.social{position:absolute;left:844px;top:38px;display:flex;gap:13px}
.social span{width:36px;height:36px;display:block}
</style>
</head>
<body>

<header class="wrap site-header">
  <div class="brand"><span class="brand-mark"></span><span class="brand-name">Vingtorget</span></div>
  <nav class="account-links"><span>REGISTER</span><span>LOGIN</span><span>UPLOAD AD</span><span>CHANGE AD</span></nav>
</header>

<nav class="wrap main-nav">
  <span class="item active">AIRPLANES</span>
  <span class="item" style="left:167px">HELICOPTERS</span>
  <span class="item" style="left:332px">PARTS</span>
  <span class="item" style="left:441px">LITERATURE</span>
  <span class="item" style="left:591px">MISC</span>
  <div class="search">Search..
    <svg width="14" height="14" viewBox="0 0 14 14"><circle cx="6" cy="6" r="4.5" fill="none" stroke="#999" stroke-width="1.6"/><line x1="9.3" y1="9.3" x2="13" y2="13" stroke="#999" stroke-width="1.8"/></svg>
  </div>
</nav>

<section class="wrap intro">
  <h1>Aircraft for Sale - the largest market for flights</h1>
  <p>Typi non habent claritatem insitam; est usus legentis in iis qui facit eoru m claritatem. Investigationes demonstraverunt lectores legere me lius quod ii legunt sae pius. Claritas est etiam processus dynamicus, qui sequitur mutationem consuetudium lectorum. Mirum est notare quam littera gothica, quam nunc putamus</p>
</section>

<main>
  <article class="listing" style="left:86px;top:392px">
    <div class="photo" role="img" aria-label="White light aircraft with cockpit instrument panel photos" style="background:linear-gradient(160deg,#c9ccd0,#6b6f72 60%,#3d3b38)"></div>
    <div class="head"><span class="title">Nordvinge MC-UL</span><span class="date">2013-10-04 16 : 49:39</span></div>
    <p class="desc">A unique UL machine in carbon fibaer, it makes it exceptionally easy. Empty weight 268kg Man uf. 2006, ca.260 hours, always in hangar.</p>
    <hr>
    <div class="seller"><div class="avatar" role="img" aria-label="Seller portrait" style="background:#b8a898"></div><div><div class="name">Kjell Norberg</div><dl><dt>Phone :</dt><dd>890 123 456 77</dd><dt>Email :</dt><dd>kjell@vingpost.net</dd></dl></div></div>
  </article>
  <article class="listing" style="left:447px;top:392px">
    <div class="photo" role="img" aria-label="Aerial view of red and white aircraft over fields" style="background:linear-gradient(170deg,#8a8b86,#7d6f66 55%,#9e4a55)"></div>
    <div class="head"><span class="title">Aerobatic Vika S-9</span><span class="date">2013-10-04 16 : 49:39</span></div>
    <p class="desc">A unique UL machine in carbon fibaer, it makes it exceptionally easy. Empty weight 268kg Man uf. 2006, ca.260 hours, always in hangar.</p>
    <hr>
    <div class="seller"><div class="avatar" role="img" aria-label="Seller portrait" style="background:#c9a48a"></div><div><div class="name">Kjell Norberg</div><dl><dt>Phone :</dt><dd>890 123 456 77</dd><dt>Email :</dt><dd>kjell@vingpost.net</dd></dl></div></div>
  </article>
  <article class="listing" style="left:812px;top:392px">
    <div class="photo" role="img" aria-label="Float plane on a river by a bridge" style="background:linear-gradient(170deg,#7f9a7a,#3f5a44 55%,#28413a)"></div>
    <div class="head"><span class="title">Aerobatic Vika S-9</span><span class="date">2013-10-04 16 : 49:39</span></div>
    <p class="desc">A unique UL machine in carbon fibaer, it makes it exceptionally easy. Empty weight 268kg Man uf. 2006, ca.260 hours, always in hangar.</p>
    <hr>
    <div class="seller"><div class="avatar" role="img" aria-label="Seller portrait" style="background:#a08f82"></div><div><div class="name">Kjell Norberg</div><dl><dt>Phone :</dt><dd>890 123 456 77</dd><dt>Email :</dt><dd>kjell@vingpost.net</dd></dl></div></div>
  </article>

  <article class="listing" style="left:86px;top:896px">
    <div class="photo" role="img" aria-label="Engine part and seaplane on a lake" style="background:linear-gradient(175deg,#9fb3c6,#7a8ea0 55%,#5a6472)"></div>
    <div class="head"><span class="title">Nordvinge MC-UL</span><span class="date">2013-10-04 16 : 49:39</span></div>
    <p class="desc">A unique UL machine in carbon fibaer, it makes it exceptionally easy. Empty weight 268kg Man uf. 2006, ca.260 hours, always in hangar.</p>
    <hr>
    <div class="seller"><div class="avatar" role="img" aria-label="Seller portrait" style="background:#4a3a32"></div><div><div class="name">Kjell Norberg</div><dl><dt>Phone :</dt><dd>890 123 456 77</dd><dt>Email :</dt><dd>kjell@vingpost.net</dd></dl></div></div>
  </article>
  <article class="listing" style="left:447px;top:896px">
    <div class="photo" role="img" aria-label="Aircraft in a bright hangar workshop" style="background:linear-gradient(170deg,#d8d6d2,#a3a09b 60%,#77736e)"></div>
    <div class="head"><span class="title">Aerobatic Vika S-9</span><span class="date">2013-10-04 16 : 49:39</span></div>
    <p class="desc">A unique UL machine in carbon fibaer, it makes it exceptionally easy. Empty weight 268kg Man uf. 2006, ca.260 hours, always in hangar.</p>
    <hr>
    <div class="seller"><div class="avatar" role="img" aria-label="Seller portrait" style="background:#8c6e5c"></div><div><div class="name">Kjell Norberg</div><dl><dt>Phone :</dt><dd>890 123 456 77</dd><dt>Email :</dt><dd>kjell@vingpost.net</dd></dl></div></div>
  </article>
  <article class="listing" style="left:812px;top:896px">
    <div class="photo" role="img" aria-label="Red and yellow aircraft on grass with cockpit view" style="background:linear-gradient(170deg,#7e8b6a,#9b3a2e 55%,#5c6a3a)"></div>
    <div class="head"><span class="title">Aerobatic Vika S-9</span><span class="date">2013-10-04 16 : 49:39</span></div>
    <p class="desc">A unique UL machine in carbon fibaer, it makes it exceptionally easy. Empty weight 268kg Man uf. 2006, ca.260 hours, always in hangar.</p>
    <hr>
    <div class="seller"><div class="avatar" role="img" aria-label="Seller portrait" style="background:#b49a88"></div><div><div class="name">Kjell Norberg</div><dl><dt>Phone :</dt><dd>890 123 456 77</dd><dt>Email :</dt><dd>kjell@vingpost.net</dd></dl></div></div>
  </article>

  <article class="listing" style="left:86px;top:1409px">
    <div class="photo" role="img" aria-label="Red aircraft with instrument parts" style="background:linear-gradient(170deg,#b23a3a,#8e4a48 55%,#c8c3bd)"></div>
    <div class="head"><span class="title">Nordvinge MC-UL</span><span class="date">2013-10-04 16 : 49:39</span></div>
    <p class="desc">A unique UL machine in carbon fibaer, it makes it exceptionally easy. Empty weight 268kg Man uf. 2006, ca.260 hours, always in hangar.</p>
    <hr>
    <div class="seller"><div class="avatar" role="img" aria-label="Seller portrait" style="background:#9a7860"></div><div><div class="name">Kjell Norberg</div><dl><dt>Phone :</dt><dd>890 123 456 77</dd><dt>Email :</dt><dd>kjell@vingpost.net</dd></dl></div></div>
  </article>
  <article class="listing" style="left:447px;top:1409px">
    <div class="photo" role="img" aria-label="Spare parts laid out on white sheet" style="background:linear-gradient(170deg,#e2e0dc,#bdb9b3 55%,#8e8a84)"></div>
    <div class="head"><span class="title">Aerobatic Vika S-9</span><span class="date">2013-10-04 16 : 49:39</span></div>
    <p class="desc">A unique UL machine in carbon fibaer, it makes it exceptionally easy. Empty weight 268kg Man uf. 2006, ca.260 hours, always in hangar.</p>
    <hr>
    <div class="seller"><div class="avatar" role="img" aria-label="Seller portrait" style="background:#4b4f58"></div><div><div class="name">Kjell Norberg</div><dl><dt>Phone :</dt><dd>890 123 456 77</dd><dt>Email :</dt><dd>kjell@vingpost.net</dd></dl></div></div>
  </article>
  <article class="listing" style="left:812px;top:1409px">
    <div class="photo" role="img" aria-label="Yellow gyrocopter on an airfield" style="background:linear-gradient(170deg,#a09c88,#d2c230 55%,#6a6a62)"></div>
    <div class="head"><span class="title">Aerobatic Vika S-9</span><span class="date">2013-10-04 16 : 49:39</span></div>
    <p class="desc">A unique UL machine in carbon fibaer, it makes it exceptionally easy. Empty weight 268kg Man uf. 2006, ca.260 hours, always in hangar.</p>
    <hr>
    <div class="seller"><div class="avatar" role="img" aria-label="Seller portrait" style="background:#5a5c62"></div><div><div class="name">Kjell Norberg</div><dl><dt>Phone :</dt><dd>890 123 456 77</dd><dt>Email :</dt><dd>kjell@vingpost.net</dd></dl></div></div>
  </article>
</main>

<nav class="wrap pager"><span>PREV</span><span>1</span><span>2</span><span>3</span><span>4</span><span>5</span><span>6</span><span>....</span><span>NEXT</span></nav>

<section class="wrap news">
  <h2>Latest News</h2>
  <div class="news-item">
    <div class="thumb"><div role="img" aria-label="Light aircraft parked outside a hangar" style="background:linear-gradient(170deg,#9aa6b2,#4f5a66)"></div></div>
    <div>
      <h3>Suspendisse eu erat quam. Vivamus porttitor eros quis.</h3>
      <p>Suspendisse eu erat quam. Vivamus porttitor eros quis nisi lacinia sedn uam a orci quis nisi sagittis. Etiam adipiscing, justo quis feugiat amus porttitor eros quis nisi lacinia sed interdum lorem vulputate.</p>
      <small>Posted on 02 June, 2013</small>
    </div>
  </div>
  <div class="news-item">
    <div class="thumb"><div role="img" aria-label="Red gyrocopter in flight against the sky" style="background:linear-gradient(170deg,#cfe0ee,#9dbdd8)"></div></div>
    <div>
      <h3>Tuspendisse eu erat quam. Vivamus porttitor eros.</h3>
      <p>Suspendisse eu erat quam. Vivamus porttitor eros quis nisi lacinia sedn uam a orci quis nisi sagittis. Etiam adipiscing, justo quis feugiat amus porttitor eros quis nisi lacinia sed interdum lorem vulputate.</p>
      <small>Posted on 02 June, 2013</small>
    </div>
  </div>
</section>

<aside class="wrap" style="top:0">
  <div class="ad-box">
    <span class="tag">Ads</span>
    <div class="ad">
      <h4>Kitchen Notes App</h4>
      <p>Free recipes for pasta, chicken, etc + ideas for menus, meals and more</p>
      <b>apps.examplestore.com</b>
    </div>
    <div class="ad">
      <h4>anti aging</h4>
      <p>Sharpen Memory and Attention with Brain Games Made by Scientists</p>
      <b>www.brainpath.example</b>
    </div>
    <span class="provider">PlaceAds</span>
  </div>
</aside>

<footer class="site-footer">
  <div class="links">Airplanes | Helicopters | Parts | Literature | Misc</div>
  <div class="copy">Copyrights 2013. All Rights Reserved.</div>
  <div class="social">
    <span style="background:#3b5b9a"></span>
    <span style="background:#2a9fd8"></span>
    <span style="background:#f07a1a"></span>
    <span style="background:#d8282a"></span>
  </div>
</footer>

</body>
</html>
```